Flyer für Gästehaus am Bodensee
Zielgruppe
Es soll ein Hausprospekt in Form eines Wickelfalz Fylers (Standard Format, also 10x21 cm Endformat) für ein Gästehaus erstellt werden. Die Texte sollten von Ihnen erstellt werden. Dabei können Sie gerne die Texte der Internetseite (www.gaestehaus-lorberg.de) nutzen (entsprechend angepasst). Es werden auch zahlreiche Bilder vom Gästehaus und auch von Attraktionen in der Umgebung zur Verfügung gestellt (Wolkenfach: https://ablage.wolkenfach.de/ordner?id=7K9PQrTxWmZa2LvNcYbHdFeGsJu4&art=teilen). Diese dürfen aber nur für diese Ausschreibung verwendet werden!
Aufgabenstellung
- Der Flyer soll zeitlos sein (also auch in ein paar Jahren noch funktionieren)
- Der Flyer soll das Interesse am Haus und der Umgebung wecken (einige Ausflugsziele sollten erwähnt werden).
- Die Lage (Uhldingen-Mühlhofen bzw. Unteruhldingen) muss als Vorteil verkauft werden da von hier aus sehr viele Ausflugsziele gut erreicht werden können.
- Die Lage (quasi direkt am See) sollte erkenntlich sein.
- Die fertige Datei wird als PDF (für den Druck und für das Marketing) benötigt.
- Außerdem als Word Datei in der der Kunde selbst etwas ändern kann.
- Auch die Originaldatei von Ihrer Software möchten wir bei Abschluss erhalten.
- Alle Quelldateien (Bilder, Texte, Schriftarten usw.) gehen an uns über (inkl. aller Rechte und Lizenzen).
- Bitten nehmen Sie maximal ein Appartment als Beispiel im Flyer auf (es ist nicht zwangsläufig notwendig, es geht auch ganz ohne). In keinem Fall alle Appartments auflisten.

```html
<!DOCTYPE html>
<html lang="de">
<head>
<meta charset="utf-8">
<title>Gästehaus Lorberg – Hausprospekt</title>
<link href="https://fonts.googleapis.com/css2?family=Open+Sans:wght@300;400;600;700&display=swap" rel="stylesheet">
<style>
:root{
  --bg:#f3efe4;
  --paper:#ffffff;
  --blue:#3a7dbf;
  --ink:#222222;
  --peach:#f8dfc0;
  --red:#d8323a;
  --lake:#2d6fa8;
  --sky:#9cc3e4;
  --sunset:#e8782a;
  --dusk:#3b2a22;
  --grass:#5e9a3a;
  --roof:#b2553a;
}
*{margin:0;padding:0;box-sizing:border-box}
html,body{width:1200px;height:848px;overflow:hidden;background:var(--bg);font-family:"Open Sans",Arial,sans-serif;color:var(--ink)}
.spread{position:absolute;top:219px;width:580px;height:410px;background:var(--paper);box-shadow:0 2px 8px rgba(0,0,0,.15)}
.spread--outer{left:12px}
.spread--inner{left:608px}
.photo{position:absolute}
.abs{position:absolute}
.heading{color:var(--blue);font-weight:300;font-size:10.5px;line-height:1.2;text-transform:uppercase;letter-spacing:.2px}
.body-text{font-size:6.3px;line-height:1.45}
.body-text p{margin-bottom:6px}
.brand{position:absolute;display:flex;align-items:center;gap:5px;color:var(--blue);font-weight:300;white-space:nowrap}
.brand__dot{border-radius:50%;background:var(--blue);flex:none}
.brand--large{left:400px;top:26px;font-size:17px}
.brand--large .brand__dot{width:16px;height:16px}
.brand--small{left:204px;top:93px;font-size:10px}
.brand--small .brand__dot{width:10px;height:10px}
.contact{left:204px;top:121px;font-size:6.4px;line-height:1.45;font-weight:600}
.contact p{margin-bottom:5px}
.portrait{left:313px;top:119px;width:59px;height:59px;border-radius:50%;border:2px solid var(--red);background:radial-gradient(circle at 50% 45%,#e9cdb6,#c9a98e 70%)}
.info-panel{position:absolute;left:394px;top:16px;width:170px;height:377px;background:var(--peach);padding:9px 10px}
.info-panel .heading{margin-bottom:9px}
.info-panel .body-text strong{font-weight:700}
.map{height:54px;margin:6px 0 8px;background:linear-gradient(90deg,transparent 8%,#2f93d6 20%,#2f93d6 80%,transparent 92%);border-radius:40%}
.excursions{position:absolute;left:0;top:230px;width:170px;list-style:none}
.excursions li{display:flex;align-items:center;gap:6px;height:30px;margin-bottom:3px;font-size:6.2px;line-height:1.3;color:var(--blue);font-weight:600}
.excursions .thumb{width:47px;height:28px;flex:none}
.excursions li span.txt::before{content:"• ";color:var(--red)}
.badge{position:absolute;left:328px;top:192px;width:50px;height:50px;border-radius:50%;background:var(--peach);display:flex;align-items:center;justify-content:center;text-align:center;font-size:5.6px;font-weight:700;line-height:1.25;transform:rotate(-22deg)}
.fade{background:linear-gradient(180deg,transparent 70%,#fff 100%)}
</style>
</head>
<body>

<section class="spread spread--outer" aria-label="Außenseite">
  <div class="photo" role="img" aria-label="Luftbild von Unteruhldingen mit Hafen" style="left:11px;top:15px;width:172px;height:128px;background:linear-gradient(160deg,#7aa36a 0%,#6f9a5c 35%,#2f6fa5 55%,#1d4f82 100%)"></div>
  <div class="photo" role="img" aria-label="Steg mit Schaukel im Abendrot" style="left:11px;top:151px;width:114px;height:114px;background:linear-gradient(180deg,#6b4a8f 0%,#e56a8a 45%,#f2a46d 60%,#3a3550 100%)"></div>
  <div class="photo" role="img" aria-label="Fahnen an der Uferpromenade" style="left:133px;top:151px;width:50px;height:114px;background:linear-gradient(180deg,#cfd9e3 0%,#b9c5cf 50%,#6b6f70 100%)"></div>
  <div class="photo" role="img" aria-label="Sonnenuntergang am See unter einem Baum" style="left:11px;top:273px;width:172px;height:127px;background:linear-gradient(180deg,#5a2410 0%,#e0661c 45%,#f49a2c 55%,#7a300e 80%,#2a1208 100%)"></div>

  <h2 class="heading abs" style="left:204px;top:18px;width:150px">Wann dürfen<br>wir Sie im<br>Gästehaus Lorberg<br>begrüssen?</h2>
  <div class="brand brand--small"><span class="brand__dot"></span>Gästehaus Lorberg</div>
  <div class="contact abs">
    <p>Familie Lorberg<br>Am Uferweg 7<br>88690 Uhldingen-Mühlhofen</p>
    <p>Tel. 0 75 56 / 41 28<br>Fax 0 75 56 / 41 29</p>
    <p>info@gaestehaus-lorberg.de<br>www.gaestehaus-lorberg.de</p>
  </div>
  <div class="portrait abs" role="img" aria-label="Porträt der Gastgeberin"></div>
  <div class="photo" role="img" aria-label="Garten mit Liegewiese am Haus" style="left:203px;top:202px;width:169px;height:107px;background:linear-gradient(180deg,#a9c9e8 0%,#dfe9f2 30%,#6ea44a 60%,#4d8a32 100%)"></div>
  <div class="photo" role="img" aria-label="Gästehaus mit Garten und Sonnenschirm" style="left:203px;top:315px;width:169px;height:83px;background:linear-gradient(180deg,#c4dcef 0%,#e9e3d8 35%,#b2553a 48%,#dcd6cc 60%,#5c9a3a 78%,#4a8230 100%)"></div>

  <div class="brand brand--large"><span class="brand__dot"></span>Gästehaus Lorberg</div>
  <div class="photo" role="img" aria-label="Ansicht des Gästehauses mit Balkonen" style="left:391px;top:69px;width:175px;height:141px;background:linear-gradient(180deg,#b7d0e6 0%,#b2553a 25%,#c0664a 40%,#ece7df 55%,#d8d2c8 75%,#5fa03a 82%,#4f8c30 100%)"></div>
  <div class="photo" role="img" aria-label="Schloss mit Blumengarten" style="left:391px;top:216px;width:62px;height:49px;background:linear-gradient(180deg,#a9cbe8 0%,#e6c9a8 45%,#5d9a3c 100%)"></div>
  <div class="photo" role="img" aria-label="Pfahlbauten am Seeufer" style="left:460px;top:216px;width:106px;height:49px;background:linear-gradient(180deg,#9ec4e4 0%,#c7d7e2 40%,#7a6a55 55%,#3f7d9b 100%)"></div>
  <div class="photo" role="img" aria-label="Abendstimmung am See mit Booten" style="left:391px;top:270px;width:175px;height:129px;background:linear-gradient(180deg,#2e3440 0%,#c98a4a 35%,#f0b25a 48%,#5a5f66 60%,#c98c4a 72%,#1f2328 100%)"></div>
</section>

<section class="spread spread--inner" aria-label="Innenseite">
  <div class="photo" role="img" aria-label="Gästehaus von der Gartenseite" style="left:11px;top:8px;width:188px;height:163px;background:linear-gradient(180deg,#c9def0 0%,#b2553a 22%,#c0664a 38%,#ede8e0 52%,#d9d3c9 72%,#8fb86a 88%,#ffffff 100%)"></div>
  <h2 class="heading abs" style="left:26px;top:184px">Herzlich willkommen!</h2>
  <div class="body-text abs" style="left:26px;top:204px;width:165px">
    <p>Egal, ob Sie 30 sind oder 70, ob Sie im Urlaub lieber faulenzen und die Seele baumeln lassen oder Ausflüge machen und Sport treiben – bei uns am See finden Sie das Ambiente, das dazu passt.</p>
    <p>Ob Sie geschäftlich unterwegs sind, alleine ausspannen möchten, oder mit Ihrer ganzen Familie verreisen – die herrliche Umgebung und die optimale Lage unseres Hauses öffnen unzählige Ausflugsmöglichkeiten für Groß und Klein.</p>
    <p>Unsere schöne Liegewiese und der gepflegte Garten sind das richtige Ambiente, wenn Sie sich erholen und ein wenig die Seele baumeln lassen wollen oder nach einem ereignisreichen Urlaubstag sich noch mit anderen Gästen zu einem kleinen Plausch treffen möchten.</p>
  </div>

  <h2 class="heading abs" style="left:211px;top:20px">Zimmer &amp; Appartements</h2>
  <div class="body-text abs" style="left:211px;top:40px;width:168px">
    <p>Alle Zimmer und Appartements sind komfortabel ausgestattet, damit Sie einen angenehmen und entspannten Urlaub verbringen.<br>Wir haben ausschließlich Nichtraucherzimmer. Gerne können Sie auf dem Balkon oder der Terrasse rauchen. Bitte beachten Sie außerdem, dass in unserem Haus keine Tiere gestattet sind.</p>
    <p style="color:var(--blue);font-weight:700;font-size:5px;letter-spacing:.4px;margin:8px 0 4px">AUSSTATTUNG</p>
    <p>Dusche / WC, Küche, Balkon (teilweise mit Seesicht) oder Terrasse. TV, Telefon, W-LAN, Safe</p>
  </div>
  <div class="photo" role="img" aria-label="Schlafzimmer mit Doppelbett" style="left:206px;top:158px;width:170px;height:69px;background:linear-gradient(90deg,#8a5a3a 0%,#e9e2d6 40%,#f3efe8 60%,#c98a5a 100%)"></div>
  <div class="badge">Bettwäsche<br>&amp; Handtücher<br>inklusive!</div>
  <div class="photo" role="img" aria-label="Gartenhaus im Grünen" style="left:206px;top:234px;width:73px;height:60px;background:linear-gradient(180deg,#b9d4ea 0%,#c77a3a 40%,#5e9a3a 70%,#4a8430 100%)"></div>
  <div class="photo" role="img" aria-label="Hauseingang mit Garten" style="left:284px;top:234px;width:92px;height:60px;background:linear-gradient(180deg,#b9d4ea 0%,#b2553a 30%,#efe9e0 55%,#5e9a3a 80%,#4a8430 100%)"></div>
  <div class="photo" role="img" aria-label="Wohnzimmer mit Sofa und Balkontür" style="left:206px;top:304px;width:170px;height:90px;background:linear-gradient(90deg,#7a5a3e 0%,#d9cfc0 35%,#eaf0e4 55%,#8a6448 100%)"></div>

  <div class="info-panel">
    <h2 class="heading">Ihr Zuhause<br>am Bodensee</h2>
    <div class="body-text">liegt in einer der schönsten Urlaubsgegenden der Bodensee-Region, in <strong>Unteruhldingen</strong>, zwischen Meersburg und Überlingen, <strong>nur 50 m vom See entfernt</strong>, gegenüber der Blumeninsel Mainau.</div>
    <div class="map" role="img" aria-label="Karte des Bodensees mit Lagemarkierung"></div>
    <h2 class="heading" style="margin-bottom:7px">Ihr Ausgangspunkt<br>für unzählige Ausflüge</h2>
    <div class="body-text">Die perfekte Lage unseres Ferienhauses in Uhldingen und die unmittelbare Nähe zum See bieten einen perfekten Startpunkt für Ausflüge – egal, was Sie vorhaben:</div>
    <ul class="excursions">
      <li><span class="thumb" role="img" aria-label="Pfahlbauten am See" style="background:linear-gradient(180deg,#9ec4e4,#7a6a55 55%,#3f7d9b)"></span><span class="txt">Die Pfahlbauten und die Birnau, mit einem traumhaften Blick über den gesamten Bodensee</span></li>
      <li><span class="thumb" role="img" aria-label="Altstadt Überlingen" style="background:linear-gradient(180deg,#a9cbe8,#2f8fb0 60%,#1d5f80)"></span><span class="txt">Überlingen – die alte Reichsstadt mit Fachwerkhäusern</span></li>
      <li><span class="thumb" role="img" aria-label="Insel Mainau von oben" style="background:linear-gradient(180deg,#2f6fa5,#5e9a3a 50%,#2f6fa5)"></span><span class="txt">Wellness in Überlingen oder in der Therme in Meersburg<br>Die Blumeninsel Mainau</span></li>
      <li><span class="thumb" role="img" aria-label="Tierpark im Wald" style="background:linear-gradient(180deg,#6e7a5a,#3e4a32)"></span><span class="txt">Affenhain Hochberg – besonders beliebt bei unseren kleinen Gästen</span></li>
    </ul>
  </div>
</section>

</body>
</html>
```